Lifestyle blog needs a website

I have a blog called Kite and Compass. Logo has been done and I also have the wordpress site with a theme already added to it.

The basics are there but I need design expertise to put everything together, make it look great and ready for me to go and in and start using. Basically what is there at the moment needs to be deleted and start again (not a lot - just me playing around). I am not attached to the theme and am happy to go with whatever ideas you can come up with. At the moment I am looking at 3 lifestyle categories (Fashion, Fitness, Feelings) with a contact page so not an extensive build.

Audience will be women over 40 but please don't make this 'frumpy' - it is aimed at the women who act, look and feel younger than their age and so 'pink & fluffy' and 'old & solid' is not the look I am going for.

My deepest apologies for the delay in responding to designs. I had a family matter which took meant I was unable to spend the quality time required to review. I will therefore be reviewing and deciding over this weekend. Once again, my sincere apologies.

Women over 40

• Feeling of being targeted at old market

```html
<!DOCTYPE html>
<html lang="en">
<head>
<meta charset="utf-8">
<title>Kite and Compass — Lifestyle Blog</title>
<link href="https://fonts.googleapis.com/css2?family=Oswald:wght@300;400;500&family=Open+Sans:ital,wght@0,400;0,600;1,400&family=Playfair+Display:ital@1&display=swap" rel="stylesheet">
<style>
:root{
  --red:#d0121b;
  --ink:#1d1d1d;
  --text:#555;
  --muted:#888;
  --line:#e3e3e3;
  --footer:#1b1b1b;
  --white:#fff;
}
*{box-sizing:border-box;margin:0;padding:0}
html,body{width:1200px;height:3805px;overflow:hidden;background:var(--white)}
body{position:relative;font-family:"Open Sans",Arial,sans-serif;color:var(--text)}
.abs{position:absolute}
.photo{position:absolute;display:block;overflow:hidden}

/* header */
.brand{left:96px;top:46px;width:240px;font-family:"Oswald",sans-serif;font-weight:500;font-size:44px;line-height:44px;color:var(--red);text-transform:uppercase;letter-spacing:1px}
.nav{right:96px;top:36px;display:flex;gap:30px;align-items:center;font-family:"Oswald",sans-serif;font-size:16px;text-transform:uppercase;color:var(--ink)}
.nav .active{color:var(--red)}

/* hero */
.hero-photo{left:355px;top:94px;width:845px;height:548px;
  background:
    radial-gradient(ellipse 40% 55% at 88% 30%,rgba(150,92,48,.85),transparent 70%),
    radial-gradient(ellipse 35% 30% at 55% 55%,rgba(48,74,140,.75),transparent 70%),
    radial-gradient(ellipse 45% 35% at 35% 40%,rgba(156,150,138,.8),transparent 70%),
    linear-gradient(180deg,#bfc8cf 0%,#d9cbb0 30%,#b79b77 60%,#8c7457 80%,#c9b18f 100%)}
.hero-frame{left:94px;top:231px;width:494px;height:287px;border:2px solid var(--red)}
.hero-card{left:108px;top:243px;width:480px;height:275px;background:var(--red);padding:42px 44px;color:var(--white)}
.hero-card .cat{font-size:17px;margin-bottom:8px}
.hero-card h1{font-family:"Oswald",sans-serif;font-weight:400;font-size:31px;line-height:42px;color:var(--white)}
.btn{display:inline-block;font-family:"Oswald",sans-serif;font-size:13px;text-transform:uppercase;padding:9px 20px;border:2px solid currentColor}
.hero-card .btn{margin-top:22px;color:var(--white)}
.dots{left:100px;top:561px;display:flex;gap:8px}
.dots span{width:13px;height:13px;border-radius:50%;border:2px solid #c9c9c9}
.dots span.on{border-color:var(--red)}

/* category grid */
.tile{position:absolute;overflow:hidden}
.tile-text{position:absolute;color:var(--white)}
.tile-text h2{font-family:"Oswald",sans-serif;font-weight:400;font-size:38px;line-height:1.1;color:var(--white)}
.tile-text p{font-size:13px;font-weight:600;line-height:19px;margin:6px 0 14px}
.tile-text .btn{color:var(--white);padding:7px 16px}
.newsletter-form{left:352px;top:647px;width:400px;height:238px;background:radial-gradient(ellipse at 70% 30%,#e01a23,#c60f18 70%)}
.newsletter-form .inset{position:absolute;left:18px;top:18px;right:18px;bottom:18px;border:2px solid rgba(255,255,255,.85)}
.email-field{position:absolute;left:36px;top:76px;width:322px;height:42px;background:var(--white);font-size:12px;color:#777;text-align:center;line-height:42px}
.subscribe-btn{position:absolute;left:36px;top:122px;width:322px;height:40px;background:linear-gradient(#3a3a3a,#111);color:var(--white);font-family:"Oswald",sans-serif;font-size:14px;text-transform:uppercase;text-align:center;line-height:40px}
.join{left:752px;top:647px;width:448px;height:238px;
  background:radial-gradient(ellipse 60% 70% at 30% 60%,rgba(210,214,222,.8),transparent 70%),linear-gradient(90deg,#eef0f3,#f6f6f6);
  text-align:right;padding:78px 100px 0 0}
.join .tag{font-family:"Playfair Display",serif;font-style:italic;font-size:20px;color:var(--muted)}
.join h2{font-family:"Oswald",sans-serif;font-weight:400;font-size:36px;color:var(--ink);line-height:1.1}

/* posts */
.meta{display:flex;gap:30px;font-size:11px;font-style:italic;color:var(--muted);align-items:center}
.meta span{display:flex;align-items:center;gap:7px}
.post h3{font-family:"Oswald",sans-serif;font-weight:400;font-size:24px;line-height:32px;color:var(--ink);margin-top:20px;width:380px}
.post .rule{width:68px;height:3px;background:var(--ink);margin:24px 0 28px}
.post p{font-size:12.5px;line-height:22px;width:385px}
.post .btn{margin-top:26px;color:var(--red);padding:7px 14px;font-size:12px}
.stamp{background:var(--white);font-family:"Oswald",sans-serif;font-weight:500;font-size:24px;line-height:26px;color:var(--red);text-transform:uppercase;padding:14px 16px;width:128px}

/* pagination */
.pager{left:101px;top:3344px;display:flex;gap:8px;font-size:11px;color:var(--text)}
.pager span{border:1px solid var(--line);padding:3px 9px;min-width:24px;text-align:center}

/* footer */
.site-footer{left:0;top:3438px;width:1200px;height:367px;background:var(--footer);color:#cfcfcf}
.site-footer h4{font-family:"Oswald",sans-serif;font-weight:400;font-size:17px;color:var(--white);text-transform:uppercase;margin-bottom:18px}
.site-footer .col{position:absolute;top:50px;font-size:12.5px;line-height:20px}
.signup p{width:300px}
.name-field{width:285px;height:40px;background:var(--white);color:#888;font-size:12px;line-height:40px;padding-left:14px;margin-top:18px}
.signup-btn{display:inline-block;background:var(--red);color:var(--white);font-family:"Oswald",sans-serif;font-size:13px;text-transform:uppercase;padding:10px 18px;margin-top:13px}
.links li{list-style:none;line-height:25px}
.contact li{list-style:none;display:flex;gap:12px;margin-bottom:14px;align-items:flex-start}
.social li{list-style:none;display:flex;gap:10px;align-items:center;margin-bottom:14px}
.social .ring{width:27px;height:27px;border-radius:50%;border:1.5px solid #cfcfcf}
.copyright{left:0;width:1200px;top:3755px;text-align:center;font-size:12px;color:#bdbdbd}
</style>
</head>
<body>

<header>
  <div class="abs brand">Kite and<br>Compass</div>
  <nav class="abs nav">
    <span class="active">Home</span><span>About</span><span>Fashion</span><span>Fitness</span><span>Feelings</span><span>Contact Us</span>
    <svg width="20" height="20" viewBox="0 0 20 20" aria-label="Search"><circle cx="8" cy="8" r="6" fill="none" stroke="#1d1d1d" stroke-width="2.4"/><line x1="12.5" y1="12.5" x2="18" y2="18" stroke="#1d1d1d" stroke-width="2.6"/></svg>
  </nav>
</header>

<section class="hero">
  <div class="photo hero-photo" role="img" aria-label="Woman in sunglasses and boots sitting on rocks by the sea"></div>
  <div class="abs hero-frame"></div>
  <div class="abs hero-card">
    <div class="cat">Fashion</div>
    <h1>Quis autem vel eum iure qui in ea voluptate velit esse quam</h1>
    <span class="btn">Read More</span>
  </div>
  <div class="abs dots"><span class="on"></span><span></span><span></span></div>
</section>

<section class="categories">
  <div class="tile" style="left:0;top:647px;width:352px;height:639px;background:radial-gradient(ellipse 45% 30% at 60% 45%,rgba(230,120,80,.75),transparent 70%),radial-gradient(ellipse 50% 45% at 55% 55%,rgba(190,140,110,.6),transparent 70%),linear-gradient(160deg,#3b3b3b,#1e1e1e 60%,#2a2320)" role="img" aria-label="Fitness model in sports top against dark background"></div>
  <div class="tile-text" style="left:18px;top:958px;width:300px">
    <h2>Fitness</h2>
    <p>Quis autem vel eum iure reprehenderit qui in ea voluptate velit esse quam nihil</p>
    <span class="btn">Read More</span>
  </div>

  <div class="tile newsletter-form">
    <div class="inset"></div>
    <div class="email-field">Email address</div>
    <div class="subscribe-btn">Subscribe</div>
  </div>

  <div class="tile join" role="img" aria-label="Light team photo behind newsletter invitation">
    <div class="tag">Best team ever</div>
    <h2>Join our Newsletter</h2>
  </div>

  <div class="tile" style="left:352px;top:885px;width:400px;height:401px;background:radial-gradient(ellipse 30% 18% at 55% 12%,rgba(40,30,30,.8),transparent 75%),radial-gradient(ellipse 40% 35% at 45% 70%,rgba(70,100,150,.75),transparent 70%),radial-gradient(ellipse 30% 40% at 75% 75%,rgba(200,140,100,.8),transparent 70%),linear-gradient(180deg,#9fb2c2,#c9a688 50%,#9c7252)" role="img" aria-label="Smiling woman in a black hat and denim jacket"></div>

  <div class="tile" style="left:752px;top:885px;width:448px;height:401px;background:radial-gradient(ellipse 60% 25% at 65% 95%,rgba(60,55,45,.85),transparent 75%),linear-gradient(180deg,#9dbcc4 0%,#5f8c78 35%,#3e6a58 65%,#6f9aa0 85%,#4a4a40 100%)" role="img" aria-label="Woman in a yoga pose on rocks above a lake"></div>
  <div class="tile-text" style="left:790px;top:1080px;width:300px">
    <h2>Feelings</h2>
    <p>Quis autem vel eum iure reprehenderit qui in ea voluptate velit esse quam nihil</p>
    <span class="btn">Read More</span>
  </div>
</section>

<main class="posts">
  <!-- post one -->
  <div class="photo" style="left:190px;top:1367px;width:477px;height:374px;background:radial-gradient(ellipse 25% 30% at 65% 40%,rgba(60,90,160,.7),transparent 70%),radial-gradient(ellipse 30% 25% at 45% 65%,rgba(235,235,230,.7),transparent 70%),linear-gradient(180deg,#4f7a2e 0%,#7fa84a 35%,#a8c671 65%,#6c8f3c 100%)" role="img" aria-label="Couple exercising outdoors on grass"></div>
  <div class="photo" style="left:0;top:1629px;width:436px;height:241px;background:radial-gradient(ellipse 30% 45% at 42% 55%,rgba(150,110,90,.6),transparent 70%),linear-gradient(120deg,#ececec,#dcdcdc 60%,#cfcfcf)" role="img" aria-label="Woman training with dumbbells"></div>
  <article class="abs post" style="left:723px;top:1396px">
    <div class="meta">
      <span><svg width="11" height="11" viewBox="0 0 11 11"><rect x=".5" y="1.5" width="10" height="9" fill="none" stroke="#888"/><line x1=".5" y1="4" x2="10.5" y2="4" stroke="#888"/></svg>Jan 25, 2018</span>
      <span><svg width="12" height="11" viewBox="0 0 12 11"><path d="M1 1h10v6H5l-3 3V7H1z" fill="none" stroke="#888"/></svg>2 comments</span>
      <span><svg width="11" height="11" viewBox="0 0 11 11"><line x1="1" y1="10" x2="10" y2="1" stroke="#888" stroke-width="1.6"/></svg>by Nora</span>
    </div>
    <h3>Quis autem vel eum iure reprehenderit qui in ea voluptate velit esse quam nihil</h3>
    <div class="rule"></div>
    <p>Sed ut perspiciatis unde omnis iste natus error sit voluptatem accusantium doloremque laudantium, totam rem aperiam, eaque ipsa quae ab illo inventore veritatis et quasi architecto beatae vitae dicta sunt explicabo.</p>
    <span class="btn">Read More</span>
  </article>

  <!-- post two -->
  <article class="abs post" style="left:96px;top:1952px">
    <div class="meta">
      <span><svg width="11" height="11" viewBox="0 0 11 11"><rect x=".5" y="1.5" width="10" height="9" fill="none" stroke="#888"/><line x1=".5" y1="4" x2="10.5" y2="4" stroke="#888"/></svg>Jan 25, 2018</span>
      <span><svg width="12" height="11" viewBox="0 0 12 11"><path d="M1 1h10v6H5l-3 3V7H1z" fill="none" stroke="#888"/></svg>2 comments</span>
      <span><svg width="11" height="11" viewBox="0 0 11 11"><line x1="1" y1="10" x2="10" y2="1" stroke="#888" stroke-width="1.6"/></svg>by Nora</span>
    </div>
    <h3>Quis autem vel eum iure reprehenderit qui in ea voluptate velit esse quam nihil</h3>
    <div class="rule"></div>
    <p>Sed ut perspiciatis unde omnis iste natus error sit voluptatem accusantium doloremque laudantium, totam rem aperiam, eaque ipsa quae ab illo inventore veritatis et quasi architecto beatae vitae dicta sunt explicabo.</p>
    <span class="btn">Read More</span>
  </article>
  <div class="photo" style="left:551px;top:1837px;width:479px;height:375px;background:radial-gradient(ellipse 22% 14% at 55% 18%,rgba(35,28,26,.85),transparent 75%),radial-gradient(ellipse 30% 35% at 60% 50%,rgba(170,110,80,.7),transparent 70%),linear-gradient(160deg,#d9c6ad,#a7876b 45%,#5e4436 80%,#3b2c24)" role="img" aria-label="Woman in a wide hat on a city street"></div>
  <div class="photo" style="left:761px;top:2101px;width:439px;height:238px;background:radial-gradient(ellipse 18% 45% at 62% 60%,rgba(150,110,90,.6),transparent 75%),radial-gradient(ellipse 18% 45% at 85% 60%,rgba(230,190,180,.8),transparent 75%),linear-gradient(90deg,#efefef 0%,#ececec 35%,#d8c6b8 60%,#ead8cc 100%)" role="img" aria-label="Two women in spring coats"></div>
  <div class="abs stamp" style="left:790px;top:2170px">Kite and Compass</div>

  <!-- post three -->
  <div class="photo" style="left:190px;top:2334px;width:480px;height:292px;background:radial-gradient(ellipse 25% 30% at 75% 80%,rgba(80,120,190,.8),transparent 70%),radial-gradient(ellipse 25% 25% at 55% 40%,rgba(210,170,140,.8),transparent 70%),linear-gradient(150deg,#f1efea,#ddd5c8 50%,#c8c2b8)" role="img" aria-label="Relaxed woman stretching on a sofa"></div>
  <div class="photo" style="left:0;top:2595px;width:439px;height:241px;background:radial-gradient(ellipse 22% 30% at 48% 40%,rgba(205,160,130,.85),transparent 70%),radial-gradient(ellipse 30% 30% at 48% 95%,rgba(70,85,55,.9),transparent 75%),radial-gradient(ellipse 25% 35% at 48% 30%,rgba(110,80,55,.7),transparent 75%),linear-gradient(130deg,#f3f1ee,#e8e4df)" role="img" aria-label="Smiling woman in a green top"></div>
  <article class="abs post" style="left:723px;top:2419px">
    <div class="meta">
      <span><svg width="11" height="11" viewBox="0 0 11 11"><rect x=".5" y="1.5" width="10" height="9" fill="none" stroke="#888"/><line x1=".5" y1="4" x2="10.5" y2="4" stroke="#888"/></svg>Jan 25, 2018</span>
      <span><svg width="12" height="11" viewBox="0 0 12 11"><path d="M1 1h10v6H5l-3 3V7H1z" fill="none" stroke="#888"/></svg>2 comments</span>
      <span><svg width="11" height="11" viewBox="0 0 11 11"><line x1="1" y1="10" x2="10" y2="1" stroke="#888" stroke-width="1.6"/></svg>by Nora</span>
    </div>
    <h3>Quis autem vel eum iure reprehenderit qui in ea voluptate velit esse quam nihil</h3>
    <div class="rule"></div>
    <p>Sed ut perspiciatis unde omnis iste natus error sit voluptatem accusantium doloremque laudantium, totam rem aperiam, eaque ipsa quae ab illo inventore veritatis et quasi architecto beatae vitae dicta sunt explicabo.</p>
    <span class="btn">Read More</span>
  </article>

  <!-- post four -->
  <article class="abs post" style="left:119px;top:2924px">
    <div class="meta">
      <span><svg width="11" height="11" viewBox="0 0 11 11"><rect x=".5" y="1.5" width="10" height="9" fill="none" stroke="#888"/><line x1=".5" y1="4" x2="10.5" y2="4" stroke="#888"/></svg>Jan 25, 2018</span>
      <span><svg width="12" height="11" viewBox="0 0 12 11"><path d="M1 1h10v6H5l-3 3V7H1z" fill="none" stroke="#888"/></svg>2 comments</span>
      <span><svg width="11" height="11" viewBox="0 0 11 11"><line x1="1" y1="10" x2="10" y2="1" stroke="#888" stroke-width="1.6"/></svg>by Nora</span>
    </div>
    <h3>Quis autem vel eum iure reprehenderit qui in ea voluptate velit esse quam nihil</h3>
    <div class="rule"></div>
    <p>Sed ut perspiciatis unde omnis iste natus error sit voluptatem accusantium doloremque laudantium, totam rem aperiam, eaque ipsa quae ab illo inventore veritatis et quasi architecto beatae vitae dicta sunt explicabo.</p>
    <span class="btn">Read More</span>
  </article>
  <div class="photo" style="left:551px;top:2813px;width:479px;height:376px;background:radial-gradient(ellipse 22% 30% at 35% 55%,rgba(215,160,110,.8),transparent 70%),radial-gradient(ellipse 22% 30% at 72% 45%,rgba(190,130,90,.8),transparent 70%),radial-gradient(ellipse 50% 20% at 70% 10%,rgba(230,190,120,.7),transparent 75%),linear-gradient(170deg,#6f5a48,#4a3e36 50%,#3a3634 80%,#5a5652)" role="img" aria-label="Couple doing push-ups in a gym"></div>
  <div class="photo" style="left:761px;top:3077px;width:439px;height:241px;background:radial-gradient(ellipse 16% 35% at 78% 55%,rgba(30,100,100,.85),transparent 75%),radial-gradient(ellipse 20% 25% at 80% 85%,rgba(90,95,100,.8),transparent 75%),linear-gradient(90deg,#e8e8e8 0%,#e2e2e2 35%,#c2c6c8 65%,#a9b1b3 100%)" role="img" aria-label="Woman in a teal sweater jumping"></div>
  <div class="abs stamp" style="left:795px;top:3150px">Kite and Compass</div>

  <nav class="abs pager">
    <span>Prev</span><span>1</span><span>2</span><span>3</span><span>4</span><span>5</span><span>6</span><span>…</span><span>22</span><span>Next</span>
  </nav>
</main>

<footer class="abs site-footer">
  <div class="col signup" style="left:99px">
    <h4>Sign up to receive email</h4>
    <p>Excepteur sint occaecat cupidatat non proident, sunt in culpa qui Nemo enim ipsum voluptatem</p>
    <div class="name-field">Enter Name</div>
    <span class="signup-btn">Subscribe</span>
  </div>
  <div class="col links" style="left:505px">
    <h4>Quick Links</h4>
    <ul><li>Home</li><li>About Me</li><li>Blog</li><li>Fashion</li><li>Fitness</li><li>Contact Us</li></ul>
  </div>
  <div class="col contact" style="left:703px">
    <h4>Contact Us</h4>
    <ul>
      <li><svg width="14" height="18" viewBox="0 0 14 18"><path d="M7 1a6 6 0 0 1 6 6c0 4-6 10-6 10S1 11 1 7a6 6 0 0 1 6-6z" fill="#cfcfcf"/><circle cx="7" cy="7" r="2.2" fill="#1b1b1b"/></svg><span>418 Harbor Lane, Suite 12<br>Lakeside CA 90001</span></li>
      <li><svg width="14" height="14" viewBox="0 0 14 14"><path d="M3 1l3 3-2 2c1 2 2 3 4 4l2-2 3 3-2 2C6 13 1 8 1 3z" fill="#cfcfcf"/></svg><span>Phone: (555) 014-2290</span></li>
      <li><svg width="14" height="11" viewBox="0 0 14 11"><rect x="0" y="0" width="14" height="11" fill="#cfcfcf"/><path d="M0 0l7 6 7-6" fill="none" stroke="#1b1b1b" stroke-width="1.2"/></svg><span>hello@kiteandcompass.com</span></li>
    </ul>
  </div>
  <div class="col social" style="left:1000px">
    <h4>Social Media</h4>
    <ul>
      <li><span class="ring"></span>Community</li>
      <li><span class="ring"></span>Updates</li>
      <li><span class="ring"></span>Circles</li>
      <li><span class="ring"></span>Video</li>
    </ul>
  </div>
</footer>
<div class="abs copyright">Copyright © Kite and Compass 2018. All rights reserved.</div>

</body>
</html>
```